American cannabis tech company business card design

Thrum.com is seeking a modern, professional, and brand-aligned business card that represents our company and its core values: Mission, Story, Values, and Impact. As an innovative cannabis company, we want a business card that is not only visually appealing but also serves as a representation of who we are and what we stand for.

Project Scope: Design a double-sided business card that integrates our brand identity and core values. Incorporate our key brand elements, ensuring a sleek and contemporary aesthetic. Visually reflect our core values (Mission, Story, Values, Impact) in a way that is engaging yet professional.

Target Market(s)

Vendors, third parties,

Contact Information for Business Card

Contact details (name, title, email, phone, website, etc.)

Font styles to use
Other font styles liked:
• Caslon, Centra

Colors

Designer to choose colors to be used in the design.

Requirements
Must have
• Thrum.com logo and branding A creative yet clean way to integrate our core values (Mission, Story, Values, Impact) Modern typography and a well-structured layout
Nice to have
• forest green, grey, white, black
Should not have
• references to marijuana, leafs, plants, or related product

```html
<!DOCTYPE html>
<html lang="en">
<head>
<meta charset="utf-8">
<title>Thrum.com Business Card</title>
<link rel="stylesheet" href="https://fonts.googleapis.com/css2?family=Roboto:wght@300;400;700;900&display=swap">
<style>
  :root {
    --forest: #1f4a26;
    --forest-dark: #173a1d;
    --ink: #050505;
    --paper: #f1f1f1;
    --paper-shade: #dcdcdc;
    --stage: #d8d5cf;
    --line-light: #e6e6e6;
  }
  * { margin: 0; padding: 0; box-sizing: border-box; }
  html, body {
    width: 1200px; height: 917px; overflow: hidden;
    background: var(--stage);
    font-family: "Roboto", sans-serif;
  }
  .sheet {
    width: 1200px; height: 917px;
    display: flex; flex-direction: column; align-items: center; justify-content: center;
    gap: 48px;
  }
  .card {
    width: 640px; height: 366px;
    border-radius: 22px; overflow: hidden;
    box-shadow: 0 10px 26px rgba(0,0,0,0.25);
    display: block;
  }
  .wordmark {
    font-family: "Roboto", sans-serif;
    font-weight: 900;
    fill: var(--forest);
    letter-spacing: 2px;
  }
  .person-name { font-weight: 700; font-size: 17px; fill: #fff; letter-spacing: 0.3px; }
  .person-title { font-weight: 300; font-size: 14px; fill: #fff; }
  .contact { font-weight: 400; font-size: 14px; fill: #fff; }
  .site-spaced { font-weight: 400; font-size: 15px; fill: #fff; letter-spacing: 9px; }
  .site-plain { font-weight: 300; font-size: 15px; fill: #fff; letter-spacing: 2px; }
</style>
</head>
<body>
<main class="sheet">

  <!-- Front -->
  <svg class="card card-front" viewBox="0 0 640 366" width="640" height="366" aria-label="Business card front">
    <defs>
      <linearGradient id="paperFront" x1="0" y1="0" x2="1" y2="1">
        <stop offset="0" stop-color="var(--paper-shade)"/>
        <stop offset="0.5" stop-color="var(--paper)"/>
        <stop offset="1" stop-color="var(--paper-shade)"/>
      </linearGradient>
    </defs>
    <rect class="card-base" width="640" height="366" fill="var(--ink)"/>
    <path class="accent-curve" d="M0,274 C330,262 520,170 548,0" fill="none" stroke="var(--forest)" stroke-width="6"/>
    <path class="white-panel" d="M0,0 H528 C500,150 320,250 0,262 Z" fill="url(#paperFront)"/>
    <rect class="footer-band" x="0" y="318" width="640" height="48" fill="var(--forest-dark)"/>
    <rect class="footer-rule" x="0" y="314" width="640" height="3" fill="var(--line-light)"/>

    <text class="wordmark" x="250" y="140" font-size="80" text-anchor="middle">THRUM</text>

    <g class="contact-block">
      <text class="person-name" x="310" y="270" text-anchor="end">DANIEL R. HAYES</text>
      <text class="person-title" x="310" y="289" text-anchor="end">Director</text>
      <rect class="divider" x="322" y="254" width="1.5" height="40" fill="#fff"/>
      <g class="phone-line">
        <circle cx="343" cy="264" r="7" fill="#fff"/>
        <path d="M340,260 q0,6 6,8 l1.5-1.8 -2-1.4 -1,1 q-2-1-3-3 l1-1 -1.4-2 z" fill="var(--ink)"/>
        <text class="contact" x="356" y="269">+1 405-555-0182</text>
      </g>
      <g class="email-line">
        <circle cx="343" cy="286" r="7" fill="#fff"/>
        <rect x="339" y="283" width="8" height="6" fill="none" stroke="var(--ink)" stroke-width="1.2"/>
        <path d="M339,283 l4,3 4,-3" fill="none" stroke="var(--ink)" stroke-width="1.2"/>
        <text class="contact" x="356" y="291">team@thrum.com</text>
      </g>
    </g>

    <text class="site-spaced" x="320" y="348" text-anchor="middle">www.THRUM.com</text>
  </svg>

  <!-- Back -->
  <svg class="card card-back" viewBox="0 0 640 366" width="640" height="366" aria-label="Business card back">
    <defs>
      <linearGradient id="paperBack" x1="0" y1="0" x2="1" y2="1">
        <stop offset="0" stop-color="var(--paper-shade)"/>
        <stop offset="0.5" stop-color="var(--paper)"/>
        <stop offset="1" stop-color="var(--paper-shade)"/>
      </linearGradient>
    </defs>
    <rect class="card-base" width="640" height="366" fill="var(--ink)"/>
    <path class="accent-curve" d="M0,318 C240,300 470,230 640,20" fill="none" stroke="var(--forest)" stroke-width="6"/>
    <path class="white-panel" d="M0,0 H640 V8 C470,220 240,290 0,304 Z" fill="url(#paperBack)"/>

    <text class="wordmark" x="260" y="145" font-size="84" text-anchor="middle">THRUM</text>

    <text class="site-plain" x="40" y="348">www.THRUM.com</text>

    <g class="social-links" fill="#fff">
      <rect x="530" y="330" width="20" height="20" rx="4"/>
      <rect x="560" y="330" width="20" height="20" rx="4"/>
      <rect x="590" y="330" width="20" height="20" rx="4"/>
    </g>
  </svg>

</main>
</body>
</html>
```